Strovanex Bootcamp Schedule

Nothing complicated just a basic (but well designed) bootcamp schedule in the form of a flyer to hand out.

Explanation below:

We hand out our fitness bootcamp schedule to potential clients and members on a regular basis and want to make a good impression about who we are and the detail we put into our material and services. I've attached a current schedule that we send out. I'm hoping we can get this as a PSD file so we can change the times and days as needed as our company grows. I've also attached a jpeg of our new website design and what that will look like along with our Strovanex Personal Training Studio logo and our Strovanex Bootcamps logo. The schedule is for our bootcamp. I also included several photos of our facility and if you want pictures of anything up close or anything that you would want in the design I can snap a good photo and send it. I included an attempt of my own to make a schedule that I wasn't too fond of but tried :)

Industry/Entity Type

Fitness

```html
<!DOCTYPE html>
<html lang="en">
<head>
<meta charset="utf-8">
<title>Strovanex Bootcamp Schedule</title>
<link rel="stylesheet" href="https://fonts.googleapis.com/css2?family=Graduate&family=Source+Sans+3:wght@600;700;900&display=swap">
<style>
  :root {
    --turf-light: #3f9a3c;
    --turf-dark: #2b7a2c;
    --gym-dark: #2a2a2e;
    --orange: #f6a321;
    --row-a: #fcf09a;
    --row-b: #fdf6c4;
    --ink: #1c1c1c;
    --white: #ffffff;
    --cell-line: #c98c1a;
  }
  * { box-sizing: border-box; margin: 0; padding: 0; }
  html, body { width: 942px; height: 1200px; overflow: hidden; }
  body { font-family: "Source Sans 3", Arial, sans-serif; color: var(--ink); }

  .flyer { position: relative; width: 942px; height: 1200px; overflow: hidden; }

  .facility-photo {
    position: absolute; inset: 0;
    background: linear-gradient(180deg, var(--gym-dark) 0%, #3b3d3f 14%, #3a7d37 24%, var(--turf-light) 45%, var(--turf-dark) 100%);
  }

  .brand-name {
    position: absolute; left: 96px; top: 128px; width: 420px;
    font-weight: 900; font-size: 50px; line-height: 1.05;
    color: var(--white); text-transform: uppercase; letter-spacing: 1px;
  }

  .title-band { position: absolute; background: var(--orange); }
  .title-band--top { left: 206px; top: 377px; width: 436px; height: 78px; }
  .title-band--main { left: 106px; top: 454px; width: 659px; height: 134px; }

  .title-word {
    position: absolute; font-family: "Graduate", Georgia, serif; font-weight: 400; color: var(--white);
    -webkit-text-stroke: 2px var(--ink); paint-order: stroke fill;
    text-shadow: 3px 3px 0 var(--ink); text-align: center; line-height: 1;
  }
  .title-word--fitness { left: 206px; top: 386px; width: 436px; font-size: 62px; }
  .title-word--bootcamp { left: 106px; top: 476px; width: 659px; font-size: 94px; }

  .kettlebell-art {
    position: absolute; left: 700px; top: 277px; width: 146px; height: 212px;
    background: radial-gradient(circle closest-side at 50% 60%, var(--white) 0%, #efefef 75%, rgba(255,255,255,0) 100%);
  }

  .schedule-label {
    position: absolute; left: 24px; top: 700px; width: 56px; height: 312px;
    display: flex; align-items: center; justify-content: center;
  }
  .schedule-label span {
    display: block; transform: rotate(-90deg); white-space: nowrap;
    font-family: "Graduate", Georgia, serif; font-size: 46px; letter-spacing: 2px;
    color: var(--orange); -webkit-text-stroke: 2px var(--white); paint-order: stroke fill;
  }

  .schedule-table {
    position: absolute; left: 101px; top: 636px; width: 813px;
    border-collapse: collapse; font-weight: 700; font-size: 23px;
  }
  .schedule-table th {
    background: var(--orange); height: 59px; font-weight: 700; font-size: 26px;
    border-right: 1px solid var(--cell-line);
  }
  .schedule-table td {
    height: 53.5px; padding: 0 12px; border-top: 1px solid var(--white);
    border-right: 1px solid var(--cell-line); white-space: nowrap;
  }
  .schedule-table tr:nth-child(odd) td { background: var(--row-a); }
  .schedule-table tr:nth-child(even) td { background: var(--row-b); }
  .col-day { width: 164px; }
  .col-am { width: 332px; text-align: center; }
  .col-pm { width: 317px; text-align: center; }
  .col-am--left { text-align: left; padding-left: 17px !important; }
  .closed-cell { display: flex; justify-content: space-between; align-items: center; height: 53.5px; }

  .length-note {
    position: absolute; left: 318px; top: 1084px; width: 528px; height: 100px;
    background: var(--ink); border: 4px solid var(--orange);
    transform: rotate(-2deg);
    display: flex; flex-direction: column; align-items: center; justify-content: center;
    font-family: "Graduate", Georgia, serif; color: var(--white); font-size: 26px; line-height: 1.25;
    text-transform: uppercase;
  }
</style>
</head>
<body>
<main class="flyer">
  <div class="facility-photo" role="img" aria-label="Photo of two people exercising on green turf in the gym"></div>

  <p class="brand-name">Strovanex<br>Bootcamps</p>

  <div class="title-band title-band--top"></div>
  <div class="title-band title-band--main"></div>
  <h1>
    <span class="title-word title-word--fitness">FITNESS</span>
    <span class="title-word title-word--bootcamp">BOOT CAMP</span>
  </h1>
  <div class="kettlebell-art" role="img" aria-label="Illustration of a white kettlebell"></div>

  <div class="schedule-label"><span>SCHEDULE</span></div>

  <table class="schedule-table">
    <thead>
      <tr><th class="col-day">Days</th><th class="col-am">Timings (AM)</th><th class="col-pm">Timings (PM)</th></tr>
    </thead>
    <tbody>
      <tr><td class="col-day">Monday</td><td class="col-am">6am, 8:30am, 12.00 noon,</td><td class="col-pm">4:30pm, 5:30pm, 6:30pm</td></tr>
      <tr><td class="col-day">Tuesday</td><td class="col-am">6am, 8:30am, 12.00 noon,</td><td class="col-pm">4:30pm, 5:30pm, 6:30pm</td></tr>
      <tr><td class="col-day">Wednesday</td><td class="col-am">6am, 8:30am, 12.00 noon,</td><td class="col-pm">4:30pm, 5:30pm, 6:30pm</td></tr>
      <tr><td class="col-day">Thursday</td><td class="col-am">6am, 8:30am, 12.00 noon,</td><td class="col-pm">4:30pm, 5:30pm, 6:30pm</td></tr>
      <tr><td class="col-day">Friday</td><td class="col-am">6am, 8:30am, 12.00 noon,</td><td class="col-pm">4:30pm, 5:30pm, 6:30pm</td></tr>
      <tr><td class="col-day">Saturday</td><td class="col-am col-am--left">9am.</td><td class="col-pm"></td></tr>
      <tr><td colspan="2"><div class="closed-cell"><span>Sunday / Major Holidays</span><span>Closed</span></div></td><td class="col-pm"></td></tr>
    </tbody>
  </table>

  <div class="length-note">
    <span>All Boot Camps</span>
    <span>are 50 minutes in length</span>
  </div>
</main>
</body>
</html>
```